REALTOR/REALESTATE INVESTOR CARD

I AM MY LOCAL CITIES FLIP THIS HOUSE KING...I CHANGE NEIGHBORHOODS ONE HOUSE AT A TIME. I BUY OLD HOUSES FOR CASH TOTALLY RENOVATE THEM TO LIKE NEW, THEN RE SELL THEM...
I HAVE BEEN USING PLATINUM & BURGANDY AS MY MAIN COLOR..
I WANT SOMETHING FUN AND MODERN TO APPEAL TO ALL BUYERS AND SELLERS. AND TO REFLECT I AM AT THE TOP OF MY GAME...A WOW...THIS IS A GREAT CARD.......WOW.......I AM A REALTOR....I FLIP HOUSES.....MAYBE SHOW AND OLD HOUSE AND THEN A SPARKLING NEW HOUSE..... MY COMPANY NAME IS HOMESTEAD CAPITAL PARTNERS THE ADDRESS IS P.O.BOX 86 CEDAR HOLLOW, S.C. 29401

Target Market(s)

I SELL HOUSES THAT HAVE BEEN RENOVATED TO ALMOST BRAND NEW CONDITION.......I ALSO BUY HOUSES/MOBILES FOR ALL CASH FAST CLOSINGS..
I BUY CEDAR HOLLOW HOUSES ALL CASH FAST CLOSE.....I BUY MOBILE HOMES ANY CONDITION, ANY PRICE.....Buyers & sellers of houses.....

Industry/Entity Type

Investment

Font styles to use
Sans Serif

Requirements
Must have
• WE BUY CEDAR HOLLOW HOMES, CASH, QUICK CLOSINGS......
RENEWING CEDAR HOLLOW, ONE HOME AT A TIME...
RAY T. BELLAMY CIAS
REALTOR/CERTIFIED INVESTOR AGENT
HOMESTEAD CAPITAL PARTNERS,LLC.
P.O. BOX 86
CEDAR HOLLOW, S.C. 29401
843-555-0172
RAYBELLAMYHOUSES@QUILLMAIL.EXAMPLE
Nice to have
• CEDAR HOLLOW'S RE-HAB KING....
A actual picture of MAYBE A HOME BEING RENOVATED
TO ONE LOOKING AWESOME.....artwork
Should not have
• a picture of and old ugly home the a sparkling brand new one that is what I di I renovate homes.......

```html
<!DOCTYPE html>
<html lang="en">
<head>
<meta charset="utf-8">
<title>Homestead Capital Partners – Business Card</title>
<link rel="stylesheet" href="https://fonts.googleapis.com/css2?family=Source+Sans+3:wght@400;600;700&display=swap">
<style>
  :root {
    --backdrop: #d2d3d5;
    --card-white: #f7f7f7;
    --platinum-light: #f4f4f5;
    --platinum-dark: #a9aaad;
    --burgundy: #8a1a2b;
    --ink: #1b1b1b;
    --tagline: #ffffff;
  }
  * { box-sizing: border-box; margin: 0; padding: 0; }
  html, body { width: 1200px; height: 1200px; overflow: hidden; }
  body {
    background: var(--backdrop);
    font-family: "Source Sans 3", Arial, sans-serif;
    position: relative;
  }
  .card {
    position: absolute;
    left: 228px;
    width: 742px;
    height: 423px;
  }
  .card-front { top: 169px; background: var(--card-white); }
  .card-back {
    top: 601px;
    background: radial-gradient(ellipse 62% 70% at 50% 52%, var(--platinum-light) 0%, #d9dadc 45%, var(--platinum-dark) 100%);
  }
  .company-name {
    position: absolute;
    color: var(--burgundy);
    font-weight: 700;
    letter-spacing: 0.2px;
    white-space: nowrap;
  }
  .card-front .company-name {
    right: 24px;
    top: 104px;
    font-size: 21px;
  }
  .card-back .company-name {
    left: 0; right: 0;
    top: 206px;
    text-align: center;
    font-size: 26px;
  }
  .agent {
    position: absolute;
    left: 62px;
    top: 262px;
    width: 260px;
    text-align: center;
  }
  .agent-name {
    font-size: 18px;
    font-weight: 700;
    color: var(--ink);
    line-height: 27px;
  }
  .agent-title {
    font-size: 18px;
    color: var(--burgundy);
    line-height: 27px;
  }
  .contact-list {
    position: absolute;
    left: 400px;
    top: 262px;
    list-style: none;
    font-size: 18px;
    color: var(--ink);
    line-height: 27px;
  }
  .contact-item {
    display: flex;
    align-items: flex-start;
    margin-bottom: 4px;
  }
  .contact-icon {
    width: 16px;
    height: 16px;
    margin-top: 5px;
    margin-right: 11px;
    flex: none;
    fill: var(--burgundy);
  }
  .tagline {
    position: absolute;
    left: 0; right: 0;
    top: 352px;
    text-align: center;
    color: var(--tagline);
    font-size: 16.5px;
    line-height: 27px;
    text-transform: uppercase;
    letter-spacing: 0.3px;
  }
</style>
</head>
<body>
  <section class="card card-front" aria-label="Card front">
    <div class="company-name">HOMESTEAD CAPITAL PARTNERS,LLC</div>

    <div class="agent">
      <div class="agent-name">RAY T. BELLAMY CIAS</div>
      <div class="agent-title">Realtor/Certified Investor Agent</div>
    </div>

    <ul class="contact-list">
      <li class="contact-item">
        <svg class="contact-icon" viewBox="0 0 16 16" aria-hidden="true">
          <path d="M8 1 L0.5 7.5 H2.5 V14 H6.5 V10 H9.5 V14 H13.5 V7.5 H15.5 Z"/>
        </svg>
        <span>P.O Box 86 Cedar Hollow<br>S.C. 29401</span>
      </li>
      <li class="contact-item">
        <svg class="contact-icon" viewBox="0 0 16 16" aria-hidden="true">
          <path d="M3.6 1.2 L5.8 1 L7 4.6 L5.3 5.8 C6.1 7.6 7.9 9.5 10 10.6 L11.3 9 L15 10.3 L14.7 12.5 C14.4 13.9 13 14.8 11.6 14.5 C6.5 13.4 2.3 9.3 1.3 4.3 C1 2.9 2.1 1.4 3.6 1.2 Z"/>
        </svg>
        <span>843-555-0172</span>
      </li>
      <li class="contact-item">
        <svg class="contact-icon" viewBox="0 0 16 16" aria-hidden="true">
          <path d="M1 3.5 H15 V13 H1 Z M1.8 4.3 L8 9 L14.2 4.3" stroke="#f7f7f7" stroke-width="1.2"/>
        </svg>
        <span>raybellamyhouses@quillmail.example</span>
      </li>
    </ul>
  </section>

  <section class="card card-back" aria-label="Card back">
    <div class="company-name">HOMESTEAD CAPITAL PARTNERS,LLC</div>
    <p class="tagline">We buy Cedar Hollow homes, cash, quick closings......<br>Renewing Cedar Hollow, one home at a time...</p>
  </section>
</body>
</html>
```